Carers Together Circle Business Cards

The Carers Together Circle provides Continuing Professional Development opportunities to Nurses both online and via exciting Travel adventures to fabulous destinations worldwide.

We require business cards for our staff and at a minimum, the card will need:

Full Name
Position
p 07 5928 6247
m 0411 222 333 (optional)
e info@wardlinkgroup.example
w www.wardlinkgroup.example

I will need a template so that I can edit different employee details as they come and go.

Here is our website - www.wardlinkgroup.example, so you can see what we are about.

I have attached our logo and if you need to know these are the colours we use on our website - orange #F4701D, Purple #6A136A and green #63AB32

Let me know if you need further details, I look forward to seeing your designs.

Cheers,
Marta.

Industry/Entity Type

Business

```html
<!DOCTYPE html>
<html lang="en">
<head>
<meta charset="utf-8">
<title>Carers Together Circle – Business Cards</title>
<link href="https://fonts.googleapis.com/css2?family=Nunito:wght@800&family=Open+Sans:wght@400;600&display=swap" rel="stylesheet">
<style>
  :root {
    --purple: #6a136a;
    --orange: #f4701d;
    --paper: #ffffff;
    --backdrop: #e9e9eb;
    --ink: #4a4a4a;
    --ink-soft: #6b6b6b;
  }
  * { box-sizing: border-box; margin: 0; padding: 0; }
  html, body { width: 1200px; height: 800px; overflow: hidden; }
  body {
    background: var(--backdrop);
    font-family: "Open Sans", Arial, sans-serif;
    display: flex;
    align-items: center;
    justify-content: center;
    gap: 40px;
  }
  .card {
    position: relative;
    width: 540px;
    height: 308px;
    background: var(--paper);
    overflow: hidden;
    box-shadow: 0 6px 18px rgba(0,0,0,0.12);
  }
  .card__art { position: absolute; inset: 0; width: 100%; height: 100%; }

  .brand {
    position: absolute;
    display: flex;
    align-items: center;
    gap: 12px;
    color: var(--purple);
    font-weight: 400;
    line-height: 1.05;
  }
  .brand__dot {
    border-radius: 50%;
    background: var(--purple);
    flex: none;
  }

  .card--front .brand { left: 50%; top: 50%; transform: translate(-50%, -50%); }
  .card--front .brand__dot { width: 60px; height: 60px; }
  .card--front .brand__name { font-size: 32px; }

  .card--back .brand { left: 28px; top: 136px; }
  .card--back .brand__dot { width: 34px; height: 34px; }
  .card--back .brand__name { font-size: 19px; width: 120px; }

  .person {
    position: absolute;
    right: 84px;
    top: 46px;
  }
  .person__name {
    font-family: "Nunito", Arial, sans-serif;
    font-weight: 800;
    font-size: 24px;
    color: var(--orange);
    line-height: 1;
  }
  .person__role {
    font-size: 12px;
    color: var(--ink-soft);
    margin-top: 2px;
    margin-left: 22px;
  }

  .contact {
    position: absolute;
    left: 196px;
    top: 108px;
    list-style: none;
    font-size: 12px;
    color: var(--ink);
  }
  .contact__item {
    display: flex;
    align-items: center;
    gap: 10px;
    height: 19px;
  }
  .contact__icon { width: 12px; height: 12px; fill: var(--ink); flex: none; }
  .contact__icon--line { fill: none; stroke: var(--ink); stroke-width: 1; }
</style>
</head>
<body>

  <section class="card card--front" aria-label="Business card front">
    <svg class="card__art" viewBox="0 0 540 308" aria-hidden="true">
      <polygon points="470,0 540,0 540,34" fill="var(--purple)"/>
      <line x1="458" y1="0" x2="540" y2="40" stroke="var(--orange)" stroke-width="2"/>
      <polygon points="0,274 0,308 70,308" fill="var(--purple)"/>
      <line x1="0" y1="268" x2="82" y2="308" stroke="var(--orange)" stroke-width="2"/>
    </svg>
    <div class="brand">
      <span class="brand__dot"></span>
      <span class="brand__name">Carers Together<br>Circle</span>
    </div>
  </section>

  <section class="card card--back" aria-label="Business card back">
    <svg class="card__art" viewBox="0 0 540 308" aria-hidden="true">
      <polygon points="170,308 540,140 540,308" fill="var(--purple)"/>
      <polygon points="330,308 540,178 540,232" fill="var(--orange)"/>
    </svg>

    <div class="person">
      <p class="person__name">Dana Wells</p>
      <p class="person__role">Director</p>
    </div>

    <div class="brand">
      <span class="brand__dot"></span>
      <span class="brand__name">Carers Together Circle</span>
    </div>

    <ul class="contact">
      <li class="contact__item">
        <svg class="contact__icon" viewBox="0 0 12 12" aria-hidden="true"><path d="M2.5 0.5l2 2.4-1 1.2c.7 1.5 1.8 2.6 3.3 3.3l1.2-1 2.4 2-1.2 2.1C5.5 10.3 1.7 6.5 1 1.6z"/></svg>
        <span>07 5928 6247</span>
      </li>
      <li class="contact__item">
        <svg class="contact__icon" viewBox="0 0 12 12" aria-hidden="true"><path d="M3 0h6v12H3z M4 1.5v7.5h4V1.5z"/></svg>
        <span>0411 222 333 (optional)</span>
      </li>
      <li class="contact__item">
        <svg class="contact__icon contact__icon--line" viewBox="0 0 12 12" aria-hidden="true"><rect x="0.5" y="2.5" width="11" height="7"/><path d="M0.5 2.5L6 6.8l5.5-4.3"/></svg>
        <span>info@wardlinkgroup.example</span>
      </li>
      <li class="contact__item">
        <svg class="contact__icon contact__icon--line" viewBox="0 0 12 12" aria-hidden="true"><circle cx="6" cy="6" r="5.4"/><ellipse cx="6" cy="6" rx="2.3" ry="5.4"/><path d="M0.8 6h10.4"/></svg>
        <span>www.wardlinkgroup.example</span>
      </li>
    </ul>
  </section>

</body>
</html>
```